New flavour! New packaging for Velocity Energy Drink!

We need a new packaging designed to show off our new grape flavored energy drink! It will require box design with matching sachets!

Established in 2018 we are a fully Australian owned and operated business that started out with 2 gamers that got sick and tired of sugary energy drinks OR expensive powder from the USA.

We are an energy drink in the esports and gaming space. Our new product is an energy drink in powder in boxes of 30 sachets (please see attached for product example)

Please see example 1 and 2 for our competitors product. We would ideally like to go a bit more minimalist than them but still have a great color pop on black backing.

Target Market(s)

Gamer's and esports athletes between the ages or 18-30

Font styles to use
Sans Serif
Other font styles liked:
• Helvetica

Colors
886aae
ffffff

Requirements
Must have
• Black base/background.
• Vibrant purple N in the Velocity Logo.
• Same or slightly different shades of purple for some text and highlights.
• Black, white and some shades of a vibrant purple (for the grape flavor)
• ingredients list (may need to be reformatted to suit)
• Please see attached for legislative requirements on the box and sachets.
Nice to have
• minimalist design but enough to be eye catching and somewhat playful
• Twitter: @VLCT_FUEL
• Instagram: @VLCT_FUEL
• Facebook: @VLCTFUEL
Should not have
• OTHER COLORS.
• Overly complex designs.

```html
<!DOCTYPE html>
<html lang="en">
<head>
<meta charset="utf-8">
<title>Velocity Energy Drink – Box Panels</title>
<link rel="stylesheet" href="https://fonts.googleapis.com/css2?family=Open+Sans:wght@400;600;700;800&display=swap">
<style>
  :root{
    --black:#0b0b0d;
    --black-soft:#1a1a1f;
    --purple:#886aae;
    --purple-vivid:#8a4fd6;
    --purple-deep:#5d3a94;
    --purple-line:#a58ccc;
    --white:#ffffff;
    --stage:#dcdcdc;
  }
  *{box-sizing:border-box;margin:0;padding:0}
  html,body{width:1200px;height:864px;overflow:hidden}
  body{background:var(--stage);font-family:"Open Sans",Arial,sans-serif;color:var(--white);position:relative}

  .panel{position:absolute;background:var(--black);overflow:hidden}
  .panel-top{left:50px;top:170px;width:880px;height:120px;
    background:linear-gradient(160deg,var(--purple-vivid) 0 34%,var(--black) 34.2% 100%)}
  .panel-top .brand-name{position:absolute;right:90px;top:30px;transform:rotate(180deg);
    font-size:46px;font-weight:800;letter-spacing:1px;color:var(--white);text-align:center;line-height:1}
  .panel-top .brand-sub{display:block;font-size:11px;font-weight:700;letter-spacing:4px;margin-top:4px}

  .panel-main{left:50px;top:290px;width:880px;height:400px;
    background:linear-gradient(90deg,var(--black) 0%,var(--black-soft) 60%,var(--black) 100%)}
  .panel-end{left:930px;top:290px;width:220px;height:400px;
    background:linear-gradient(115deg,var(--black) 0 55%,var(--purple-deep) 55.3% 100%)}
  .end-mark{position:absolute;left:60px;top:130px;width:100px;height:100px;border:10px solid var(--purple-vivid)}

  /* brand lockup */
  .brand{position:absolute;left:28px;top:22px}
  .brand-title{font-size:38px;font-weight:800;line-height:1;color:var(--white);letter-spacing:.5px}
  .brand-tag{font-size:10px;font-weight:700;letter-spacing:3px;color:var(--white);text-align:right;margin-top:2px}

  /* nutrition */
  .nutrition{position:absolute;left:28px;top:88px;width:250px;background:var(--purple);
    font-size:7px;line-height:10px;color:var(--white);border:1px solid var(--purple-line)}
  .nutrition h3{font-size:8.5px;line-height:12px;font-weight:700;padding:3px 5px;border-bottom:1px solid var(--purple-line);text-transform:uppercase}
  .nutrition table{width:100%;border-collapse:collapse}
  .nutrition td,.nutrition th{border:1px solid var(--purple-line);padding:1px 4px;font-weight:400;text-align:left}
  .nutrition th{font-weight:700;font-size:6px;line-height:8px;text-align:center}
  .nutrition td.val{text-align:right;width:62px}
  .nutrition tr.section td{font-weight:700}
  .best-before{position:absolute;left:28px;top:366px;width:250px;height:24px;display:flex;font-size:10px}
  .best-before .label{background:var(--purple-vivid);padding:4px 10px;width:90px}
  .best-before .value{background:var(--white);color:var(--purple);flex:1;padding:5px 10px;font-size:8.5px}

  /* info blocks */
  .info{position:absolute;left:300px;width:340px}
  .tab{display:inline-block;background:var(--purple-vivid);font-size:13px;line-height:18px;padding:3px 12px;color:var(--white)}
  .info-box{border:2px solid var(--purple-vivid);padding:9px 12px;font-size:10px;line-height:14px;font-weight:600}
  .ingredients{top:88px}
  .directions{top:232px}
  .directions .note{color:var(--purple-vivid);font-weight:600}
  .net-qty{position:absolute;left:300px;top:366px;font-size:10px;font-weight:600}

  .side-mark{position:absolute;left:700px;top:130px;width:70px;height:70px;background:var(--purple-vivid)}

  .importer{position:absolute;left:665px;top:228px;width:195px}
  .importer .tab{font-size:14px;font-weight:600}
  .importer .info-box{font-size:10.5px;line-height:15px;font-weight:400}
  .importer .web{font-size:8.5px;line-height:12px;margin-top:4px}
  .origin{font-size:9px;margin-top:4px}
</style>
</head>
<body>

  <section class="panel panel-top">
    <div class="brand-name">VELOCITY<span class="brand-sub">ENERGY DRINK</span></div>
  </section>

  <section class="panel panel-main">
    <div class="brand">
      <div class="brand-title">VELOCITY</div>
      <div class="brand-tag">ENERGY DRINK</div>
    </div>

    <div class="nutrition">
      <h3>Nutrition Information</h3>
      <table>
        <tr><td>Servings per package</td><td colspan="2">30</td></tr>
        <tr><td>Serving size</td><td colspan="2">5g powder &amp; 400 ml water</td></tr>
        <tr><td></td><th>Av quantity per serving (400 ml)</th><th>Av quantity per 100 ml</th></tr>
        <tr><td>Energy</td><td class="val">9 kJ</td><td class="val">2 kJ</td></tr>
        <tr><td>Protein</td><td class="val">0.0 g</td><td class="val">0.0 g</td></tr>
        <tr><td>Fat, total</td><td class="val">0.0 g</td><td class="val">0.0 g</td></tr>
        <tr><td>&nbsp;&nbsp;Saturated</td><td class="val">0.0 g</td><td class="val">0.0 g</td></tr>
        <tr><td>Carbohydrate</td><td class="val">0.3 g</td><td class="val">0.1 g</td></tr>
        <tr><td>&nbsp;&nbsp;Sugars</td><td class="val">0.2 g</td><td class="val">0.1 g</td></tr>
        <tr><td>Sodium</td><td class="val">250 mg</td><td class="val">63 mg</td></tr>
        <tr class="section"><td colspan="3">Composition information</td></tr>
        <tr><td>Caffeine</td><td class="val">140 mg</td><td class="val">35 mg</td></tr>
        <tr><td>Niacin (B3)</td><td class="val">10 mg</td><td class="val">2.5 mg</td></tr>
        <tr><td>Thiamin (B1)</td><td class="val">5 mg</td><td class="val">1.3 mg</td></tr>
        <tr><td>Vitamin B6</td><td class="val">4 mg</td><td class="val">1.0 mg</td></tr>
        <tr><td>Riboflavin (B2)</td><td class="val">3 mg</td><td class="val">0.8 mg</td></tr>
        <tr><td>Taurine</td><td class="val">500 mg</td><td class="val">125 mg</td></tr>
      </table>
    </div>
    <div class="best-before">
      <div class="label">Best Before</div>
      <div class="value">See base of packaging</div>
    </div>

    <div class="info ingredients">
      <span class="tab">Ingredients</span>
      <div class="info-box">Acidity regulator (citric acid, sodium citrate), mineral salt (sodium bicarbonate), taurine, natural orange juice powder (8.5%) (maltodextrin, sugar, orange juice concentrate), caffeine (2.8%), inositol, vitamins (B3, B1, B6, B2), ginseng extract (0.5%), sweetener (steviol glycoside), mineral salt (magnesium stearate).</div>
    </div>

    <div class="info directions">
      <span class="tab">Directions for Use</span>
      <div class="info-box">
        Place one tablet in 400 ml water, stir until dissolved, and consume immediately.<br>
        <span class="note">Maximum of two tablets per day.<br>
        Store in a cool dry place, away from sunlight below 25° C.<br>
        Keep away from children.</span>
      </div>
    </div>
    <div class="net-qty">Formulated Caffeinated Beverage&nbsp;&nbsp;150 g (30 x 5 g)</div>

    <div class="side-mark" aria-hidden="true"></div>

    <div class="importer">
      <span class="tab">Imported By:</span>
      <div class="info-box">
        Arcade Fuel Pty Ltd<br>
        48 Harbour Lane<br>
        Melbourne&nbsp; VIC&nbsp; 3000<br>
        Australia
        <div class="web">www.velocityfuel.shop</div>
      </div>
      <div class="origin">Made in China</div>
    </div>
  </section>

  <section class="panel panel-end">
    <div class="end-mark" aria-hidden="true"></div>
  </section>

</body>
</html>
```